A Hair, Beauty and Nails Wholesalers Needs a Business Card Design

We need a business card design for our company which is being passed from parents to daughter, so we wont to re-launch the company with an updated, modern, sophisticated, elegant, chic and fresh look which still incorporates the original colour scheme of Hot Pink, Dark Grey and White. The original logo which is attached can be used on the card but we would like to see some designs with the logo and some without, as we have not yet decided if we want the logo on the card. The name of our company is 'Velmora Supplies' and the name of our website is VelmoraGlowandPolish.example.au. We specialise in supplying a massive range of Hair, Beauty and Nail products to the industry. We are based in QLD, Australia but ship many orders via our website all across Australia.

```html
<!DOCTYPE html>
<html lang="en">
<head>
<meta charset="utf-8">
<title>Velmora Supplies – Business Card</title>
<link rel="stylesheet" href="https://fonts.googleapis.com/css2?family=Comfortaa:wght@300;400;600&display=swap">
<style>
  :root {
    --pink: #e065b4;
    --pink-soft: #ea8cc8;
    --paper: #ececec;
    --paper-shade: #e2e2e2;
  }
  html, body {
    margin: 0;
    padding: 0;
    overflow: hidden;
    background: var(--paper);
  }
  .card {
    position: relative;
    width: 1200px;
    height: 900px;
    overflow: hidden;
    background: radial-gradient(ellipse at 50% 40%, #f1f1f1 0%, var(--paper) 55%, var(--paper-shade) 100%);
    font-family: 'Comfortaa', sans-serif;
    font-weight: 300;
    color: var(--pink);
  }
  .brand-word {
    position: absolute;
    left: 20px;
    width: 410px;
    margin: 0;
    text-align: center;
    font-weight: 300;
    color: var(--pink);
    line-height: 1;
  }
  .brand-word--top { top: 130px; font-size: 80px; }
  .brand-word--bottom { top: 595px; font-size: 68px; }
  .brand-mark {
    position: absolute;
    left: 120px;
    top: 300px;
  }
  .divider {
    position: absolute;
    left: 445px;
    top: 150px;
    width: 2px;
    height: 590px;
    background: var(--pink);
  }
  .contact {
    position: absolute;
    left: 466px;
    top: 0;
    width: 715px;
  }
  .contact p {
    position: absolute;
    margin: 0;
    white-space: nowrap;
    line-height: 1;
  }
  .contact .name { top: 152px; font-size: 50px; }
  .contact .name-rule {
    position: absolute;
    top: 230px;
    left: 4px;
    width: 480px;
    height: 2px;
    background: var(--pink);
  }
  .contact .role { top: 262px; font-size: 45px; }
  .contact .street { top: 384px; font-size: 50px; }
  .contact .city { top: 464px; font-size: 50px; }
  .contact .phone { top: 602px; left: 8px; font-size: 44px; }
  .contact .email { top: 684px; left: 6px; font-size: 27px; letter-spacing: -0.2px; }
  .num { font-weight: 600; }
  .website {
    position: absolute;
    left: 0;
    right: 0;
    top: 845px;
    margin: 0;
    text-align: center;
    font-size: 28px;
    line-height: 1;
    white-space: nowrap;
  }
  .website-slash {
    position: absolute;
    top: 0;
    left: 0;
  }
</style>
</head>
<body>
<main class="card">
  <h1 class="brand-word brand-word--top">Velmora</h1>
  <svg class="brand-mark" width="210" height="210" viewBox="0 0 210 210" aria-hidden="true">
    <circle cx="105" cy="105" r="100" fill="var(--pink)"/>
  </svg>
  <p class="brand-word brand-word--bottom">Supplies</p>

  <div class="divider"></div>

  <section class="contact">
    <p class="name">Danika Marlowe</p>
    <div class="name-rule"></div>
    <p class="role">Manager, Velmora Supplies</p>
    <p class="street"><span class="num">27</span> Harlow Lane</p>
    <p class="city">Brindleton, QLD, <span class="num">4000</span></p>
    <p class="phone">Ph: <span class="num">(07) 5550 0123</span></p>
    <p class="email">Email: admin@velmoraglowandpolish.example.au</p>
  </section>

  <svg class="website-slash" width="1200" height="900" viewBox="0 0 1200 900" aria-hidden="true">
    <line x1="205" y1="900" x2="255" y2="818" stroke="var(--pink)" stroke-width="2"/>
    <line x1="965" y1="900" x2="1012" y2="818" stroke="var(--pink)" stroke-width="2"/>
  </svg>
  <p class="website">Website: www.VelmoraGlowandPolish.example.au</p>
</main>
</body>
</html>
```